Four banner campaigns, much work to come!

I want banners created for 4 campaigns.

For each campaign I need these 6 banner sizes created:

? Web Banner Sizes (300x250, 728x90, 160x600)
One of each of these sizes, so 3 web banners

? Mobile Banner Sizes (300x50, 216x36, 240x240)

Campaign 1
http://www.townshopratings.example/KVB-52917.html

Campaign 2
http://www.townshopratings.example/Rockville-MD/Velunor-48203.html

Campaign 3
http://www.nearbylistpages.example/m/orlando-fl-vacation-rentals/

Campaign 4
www.townshopratings.example/The-Hollis-Institute-of-Sound-and-Screen-Studies-73542.html

I will send you numbers to edit each banner, so the 24 banners
will have 4 variations with different numbers. Same banners just
need you to send a copy with different phone numbers.

I want the work done today and I will post my next gig for the same winner.
Updates

I just want to make sure everyone knows this project is for 4 different banner campaigns.

Given banners in each size for each campaign.  I can submit additional info links if
needed let me know.  Please post more samples as soon as possible so I can pick
a designer to finish.

Thank you!

Industry/Entity Type

Radio

Requirements
Must have
• Messaging that follows the messaging in the pages I have submitted.
Nice to have
• Animated gif banners in general, QDN compliant.

```html
<!DOCTYPE html>
<html lang="en">
<head>
<meta charset="utf-8">
<title>The Hollis Institute – Banner Set</title>
<link rel="stylesheet" href="https://fonts.googleapis.com/css2?family=Roboto+Slab:wght@400;700&family=Questrial&display=swap">
<style>
  :root {
    --backdrop: #4a4a4a;
    --backdrop-dark: #2e2e2e;
    --banner-top: #1c2a38;
    --banner-bottom: #03070b;
    --ink: #f2f4f6;
    --ink-soft: #c9ced4;
    --accent: #4fb3dc;
    --rule: #e8ecef;
    --divider: #3d4b58;
  }
  * { box-sizing: border-box; margin: 0; padding: 0; }
  html, body { width: 1200px; height: 1080px; overflow: hidden; }
  body {
    background: linear-gradient(160deg, var(--backdrop) 0%, var(--backdrop-dark) 60%, #3a3a3a 100%);
    font-family: "Questrial", Arial, sans-serif;
  }
  .stage {
    position: relative;
    width: 1000px; height: 900px;
    transform: scale(1.2);
    transform-origin: 0 0;
  }
  .banner {
    position: absolute;
    overflow: hidden;
    background: linear-gradient(180deg, var(--banner-top) 0%, #0b131b 55%, var(--banner-bottom) 100%);
    color: var(--ink);
  }
  .brand {
    font-family: "Roboto Slab", Georgia, serif;
    font-weight: 700;
    color: var(--ink-soft);
    line-height: 1.05;
  }
  .brand .brand-sub { display: block; font-size: 0.42em; letter-spacing: 0.02em; text-transform: uppercase; margin-top: 3px; }
  .headline {
    font-family: "Roboto Slab", Georgia, serif;
    font-weight: 400;
    color: var(--ink);
    line-height: 1.1;
  }
  .headline em { font-style: normal; color: var(--accent); }
  .call { color: var(--ink); white-space: nowrap; }
  .call .phone { color: var(--accent); }
  .photo { position: absolute; }

  /* 728 x 90 leaderboard */
  .leaderboard { left: 137px; top: 88px; width: 728px; height: 90px; }
  .leaderboard .brand { position: absolute; left: 13px; top: 20px; font-size: 22px; }
  .leaderboard .divider { position: absolute; left: 218px; top: 14px; height: 62px; border-left: 1px dotted var(--divider); }
  .leaderboard .headline { position: absolute; left: 249px; top: 7px; font-size: 15.5px; }
  .leaderboard .call { position: absolute; left: 249px; top: 50px; font-size: 13px; }
  .leaderboard .call .phone { font-size: 22px; }
  .leaderboard .photo {
    left: 484px; top: 0; width: 244px; height: 90px;
    border-left: 2px solid var(--rule);
    background: radial-gradient(ellipse at 50% 40%, #d9c39a 0%, #8d7450 40%, #1b1510 85%);
  }

  /* 300 x 250 medium rectangle */
  .rectangle { left: 351px; top: 214px; width: 300px; height: 250px; }
  .rectangle .brand { position: absolute; left: 9px; top: 13px; font-size: 13px; }
  .rectangle .divider { position: absolute; left: 139px; top: 10px; height: 40px; border-left: 1px dotted var(--divider); }
  .rectangle .headline { position: absolute; left: 149px; top: 15px; font-size: 11.5px; }
  .rectangle .photo {
    left: 0; top: 57px; width: 300px; height: 145px;
    border-top: 2px solid var(--rule); border-bottom: 2px solid var(--rule);
    background: linear-gradient(90deg, #3a2e2c 0%, #c24a34 25%, #8a8f94 55%, #d6dadd 85%, #b5bbbf 100%);
  }
  .rectangle .call { position: absolute; left: 0; right: 0; top: 212px; text-align: center; font-size: 13px; }
  .rectangle .call .phone { font-size: 21px; }

  /* 160 x 600 skyscraper */
  .skyscraper { left: 705px; top: 214px; width: 160px; height: 600px; }
  .skyscraper .brand { position: absolute; left: 5px; top: 16px; right: 5px; font-size: 14px; }
  .skyscraper .photo {
    left: 0; top: 72px; width: 160px; height: 367px;
    border-top: 2px solid var(--rule); border-bottom: 2px solid var(--rule);
    background: linear-gradient(160deg, #0c1622 0%, #243a52 35%, #13202e 60%, #3c4a52 85%, #1a2430 100%);
  }
  .skyscraper .headline { position: absolute; left: 0; right: 0; top: 453px; text-align: center; font-size: 11.5px; }
  .skyscraper .call { position: absolute; left: 0; right: 0; top: 494px; text-align: center; font-size: 18px; line-height: 1.2; }
  .skyscraper .call .phone { display: block; font-size: 25px; line-height: 1.2; }
</style>
</head>
<body>
<main class="stage">

  <section class="banner leaderboard" aria-label="728 by 90 banner">
    <div class="brand">The Hollis Institute<span class="brand-sub">of Sound &amp; Screen Studies</span></div>
    <div class="divider"></div>
    <p class="headline">Make the career move<br>that will <em>change your life</em>.</p>
    <p class="call">call today <span class="phone">(888) 555-0147</span></p>
    <div class="photo" role="img" aria-label="Photo of a television studio with cameras on tripods silhouetted against bright lights"></div>
  </section>

  <section class="banner rectangle" aria-label="300 by 250 banner">
    <div class="brand">The Hollis Institute<span class="brand-sub">of Sound &amp; Screen Studies</span></div>
    <div class="divider"></div>
    <p class="headline">Make the career move<br>that will <em>change your life</em>.</p>
    <div class="photo" role="img" aria-label="Photo of a smiling radio host wearing headphones at a studio microphone"></div>
    <p class="call">call today <span class="phone">(888) 555-0147</span></p>
  </section>

  <section class="banner skyscraper" aria-label="160 by 600 banner">
    <div class="brand">The Hollis Institute<span class="brand-sub">of Sound &amp; Screen Studies</span></div>
    <div class="photo" role="img" aria-label="Close-up photo of a broadcast control panel with lit buttons and red digital readouts"></div>
    <p class="headline">Make the career move<br>that will <em>change your life</em>.</p>
    <p class="call">call today <span class="phone">(888)<br>555-0147</span></p>
  </section>

</main>
</body>
</html>
```